Carpentry company Needs a business card design

We need a design for a Carpentry / building company, business card. Please think of designs out of the ordinary and try to make it eye catching. Our existing logo will need to be incorporated in the design. However feel free to change the colours of the logo to suit your design. I would like to see some designs with green /black and orange incorporated into it.These are not the only colours accepted and all designs that appeal will be accepted.

Please contact me should you have any questions
Thanks Martin

Target Market(s)

General Public seeking carpentry work

Industry/Entity Type

Business

Contact Information for Business Card

- Current company logo ( colours can be changed)
-Phone number ,
- info@brelvanbuild.com.au
- brelvanbuild.com.au
-the facebook symbol

Font styles to use
Other font styles liked:
• You choose

Requirements
Must have
• Services we provide
• - Renovations
• -Deckings & Pergolas
• -Kitchens
• - Bathrooms
• - Intricate details
Nice to have
• an awesome design
Should not have
• Tools on the business card

```html
<!DOCTYPE html>
<html lang="en">
<head>
<meta charset="utf-8">
<title>Brelvan Build – Business Card</title>
<link rel="stylesheet" href="https://fonts.googleapis.com/css2?family=Source+Sans+3:wght@400;600;700&display=swap">
<style>
  :root {
    --backdrop: #e9e7e4;
    --card-white: #ffffff;
    --brand-green: #0f780d;
    --brand-green-light: #3a9a2e;
    --ink: #231815;
    --text-light: #ffffff;
  }
  * { margin: 0; padding: 0; box-sizing: border-box; }
  html, body {
    width: 1200px; height: 900px; overflow: hidden;
    background: var(--backdrop);
    font-family: "Source Sans 3", Arial, sans-serif;
  }
  .card {
    position: absolute;
    background: var(--card-white);
    box-shadow: 0 6px 18px rgba(0,0,0,0.18);
    overflow: hidden;
  }
  .card--front { left: 77px; top: 34px; width: 589px; height: 364px; }
  .card--back  { left: 388px; top: 505px; width: 567px; height: 352px; }

  .card__header { position: absolute; left: 0; top: 0; right: 0; }
  .card--front .card__header { height: 171px; }
  .card--back .card__header { height: 148px; }

  .brand {
    position: absolute;
    display: flex; align-items: center; gap: 12px;
    color: var(--ink);
    font-weight: 700;
    letter-spacing: 2px;
    white-space: nowrap;
  }
  .card--front .brand { left: 32px; top: 62px; font-size: 42px; }
  .card--back .brand { left: 32px; top: 48px; font-size: 41px; }
  .brand__mark {
    width: 22px; height: 22px; background: var(--brand-green-light);
    flex: none;
  }

  .card__panel {
    position: absolute; left: 0; right: 0; bottom: 0;
    background: var(--brand-green);
    color: var(--text-light);
  }
  .card--front .card__panel { top: 171px; }
  .card--back .card__panel { top: 148px; }

  .person { position: absolute; left: 29px; top: 14px; }
  .person__name { font-size: 22px; font-weight: 600; line-height: 1.2; }
  .person__role { font-size: 16px; font-weight: 400; margin-top: 1px; }

  .contact { position: absolute; left: 29px; top: 92px; list-style: none; font-size: 16px; line-height: 24px; }
  .contact__label { font-weight: 700; }

  .social-square {
    position: absolute; right: 61px; top: 131px;
    width: 26px; height: 26px; border-radius: 4px;
    background: var(--text-light);
  }

  .services { position: absolute; left: 31px; top: 8px; }
  .services__title { font-size: 22px; font-weight: 700; margin-bottom: 10px; }
  .services__list { list-style: none; font-size: 16px; font-weight: 600; }
  .services__list li { height: 30px; display: flex; align-items: center; gap: 10px; }
  .services__list li::before {
    content: ""; width: 6px; height: 6px; background: var(--text-light); flex: none;
  }
</style>
</head>
<body>
  <section class="card card--front" aria-label="Business card front">
    <header class="card__header">
      <div class="brand"><span class="brand__mark"></span>BRELVAN BUILD</div>
    </header>
    <div class="card__panel">
      <div class="person">
        <p class="person__name">David Martin</p>
        <p class="person__role">Managing Director</p>
      </div>
      <ul class="contact">
        <li><span class="contact__label">T:</span> (044)-555-0142</li>
        <li><span class="contact__label">E:</span> info@brelvanbuild.com.au</li>
        <li><span class="contact__label">W:</span> www.brelvanbuild.com.au</li>
      </ul>
      <span class="social-square" aria-label="Social page"></span>
    </div>
  </section>

  <section class="card card--back" aria-label="Business card back">
    <header class="card__header">
      <div class="brand"><span class="brand__mark"></span>BRELVAN BUILD</div>
    </header>
    <div class="card__panel">
      <div class="services">
        <h2 class="services__title">Services we provide</h2>
        <ul class="services__list">
          <li>Renovations</li>
          <li>Deckings &amp; Pergolas</li>
          <li>Kitchens</li>
          <li>Bathrooms</li>
          <li>Intricate details</li>
        </ul>
      </div>
    </div>
  </section>
</body>
</html>
```